Brochure for PeakForge Gym
PeakForge Northwood
Higher Consciousness Through Harder Training
Looking for a tri fold brochure that has information about our gym. We pretty much need to put the info on WWW.Peakforgenorthwood.net into a brochure format. A good looking front cover, some info inside including prices, and the schedule on the back flap.
Sports
Young Fitness enthusiasts.
Tri Fold brochure
Our Logo

```html
<!DOCTYPE html>
<html lang="en">
<head>
<meta charset="utf-8">
<title>PeakForge Northwood – Tri-fold Brochure</title>
<link href="https://fonts.googleapis.com/css2?family=Oswald:wght@500;700&family=Open+Sans:ital,wght@0,400;0,700;1,800&display=swap" rel="stylesheet">
<style>
:root{
  --stage:#dcdcdc;
  --ink:#1b1b1b;
  --ink-soft:#262626;
  --red:#c4161c;
  --red-dark:#7d0c10;
  --white:#ffffff;
  --grey-text:#c9c9c9;
  --photo-grey:#7a7a7a;
}
*{box-sizing:border-box;margin:0;padding:0}
html,body{width:1200px;height:961px;overflow:hidden}
body{background:var(--stage);font-family:"Open Sans",Arial,sans-serif;color:var(--white);position:relative}
.spread{position:absolute;left:300px;width:600px;height:450px;display:flex;background:var(--ink);box-shadow:0 6px 18px rgba(0,0,0,.35);overflow:hidden}
.spread--outside{top:20px}
.spread--inside{top:491px}
.panel{width:200px;height:100%;position:relative;padding:16px 14px}
.panel + .panel{border-left:1px solid #333}
.heading{font-family:"Oswald",Arial,sans-serif;font-weight:700;color:var(--red);font-size:17px;line-height:1.1;margin-bottom:8px}
.body-copy{font-size:6.6px;line-height:1.5;color:var(--grey-text);margin-bottom:8px}
.photo{border-radius:2px}
/* outside: testimonials */
.photo--gym-members{height:112px;margin:6px 0 10px;background:linear-gradient(135deg,#9a8f86,#4d4540 60%,#2c2826)}
/* outside: contact */
.program-box{background:var(--red);padding:8px 10px;margin:-16px -14px 0;height:46px}
.program-box .label{font-family:"Oswald",Arial,sans-serif;font-size:10px;letter-spacing:.5px}
.price-list{list-style:none;padding:12px 0 10px}
.price-list li{font-size:9px;line-height:1.35;margin-bottom:6px;color:var(--white)}
.photo--map{height:96px;background:linear-gradient(160deg,#e8e4d8,#c9cfc2 55%,#a9b7c4)}
.address{font-size:7.5px;line-height:1.45;margin-top:10px;text-align:center}
.address strong{font-family:"Oswald",Arial,sans-serif;font-size:10px}
.emails{position:absolute;bottom:14px;left:14px;right:14px;font-size:7px;line-height:1.5;text-align:center;color:var(--grey-text)}
/* outside: cover */
.panel--cover{padding:0;background:var(--ink-soft)}
.cover-brand{height:150px;background:linear-gradient(180deg,var(--red) ,var(--red-dark));display:flex;flex-direction:column;align-items:center;justify-content:center;gap:8px;padding:0 12px}
.brand-dot{width:26px;height:26px;border-radius:50%;background:var(--white)}
.brand-name{font-family:"Oswald",Arial,sans-serif;font-weight:700;font-size:20px;text-align:center;line-height:1.1;color:var(--white)}
.tagline{font-family:"Oswald",Arial,sans-serif;font-size:8px;text-align:center;letter-spacing:.6px;text-transform:uppercase;color:var(--white)}
.photo-grid{display:grid;grid-template-columns:1fr 1fr;gap:3px;padding:10px 12px;height:246px}
.photo-grid .photo{background:linear-gradient(135deg,#b5b5b5,#555)}
.photo-grid .photo:nth-child(2n){background:linear-gradient(135deg,#8d8d8d,#2f2f2f)}
.cover-web{position:absolute;bottom:0;left:0;right:0;height:54px;background:var(--red);display:flex;align-items:center;justify-content:center;font-family:"Oswald",Arial,sans-serif;font-size:10px;letter-spacing:.4px}
/* inside */
.panel--athlete{padding:0}
.photo--athlete{position:absolute;inset:0;background:linear-gradient(120deg,#3a3a3a 0%,#9b6b55 35%,#c98f76 50%,#5a3d33 75%,#222 100%)}
.wave{position:absolute;left:0;bottom:0;width:600px;height:80px}
.slogan{position:absolute;bottom:18px;font-weight:800;font-style:italic;font-size:14px;color:var(--white)}
.slogan--start{left:16px}
.slogan--best{right:14px;font-size:12px}
</style>
</head>
<body>

<section class="spread spread--outside" aria-label="Brochure outside">
  <div class="panel panel--testimonials">
    <h2 class="heading">Testimonials</h2>
    <p class="body-copy">Training here changed how I move, eat and think. The coaches push every member to work harder than yesterday, and the community keeps you coming back. I am stronger now than I was at twenty.</p>
    <div class="photo photo--gym-members" role="img" aria-label="Photo of members training together in the gym"></div>
    <p class="body-copy">After one month of classes I dropped two sizes and found friends who cheer for every new personal record. Worth every early morning.</p>
  </div>

  <div class="panel panel--contact">
    <div class="program-box"><span class="label">PEAKFORGE PROGRAM</span></div>
    <ul class="price-list">
      <li>Single Session</li>
      <li>3 Session Introductory Package</li>
      <li>20 Session Punch Card</li>
      <li>40 Session Punch Card</li>
    </ul>
    <div class="photo photo--map" role="img" aria-label="Street map showing the gym location"></div>
    <p class="address"><strong>PeakForge Northwood</strong><br>480 Alder Ave, Northwood, NY 10990<br>www.pfnorthwood.net<br>(555) 014-2288</p>
    <p class="emails">coach.rivera@mailbox.com<br>coach.hale@mailbox.com</p>
  </div>

  <div class="panel panel--cover">
    <div class="cover-brand">
      <span class="brand-dot"></span>
      <span class="brand-name">PeakForge Northwood</span>
      <span class="tagline">Higher Consciousness Through Harder Training</span>
    </div>
    <div class="photo-grid">
      <div class="photo" role="img" aria-label="Black and white photo of an athlete lifting"></div>
      <div class="photo" role="img" aria-label="Black and white photo of kettlebells"></div>
      <div class="photo" role="img" aria-label="Black and white photo of a toned torso"></div>
      <div class="photo" role="img" aria-label="Black and white photo of a barbell"></div>
    </div>
    <div class="cover-web">WWW.Peakforgenorthwood.net</div>
  </div>
</section>

<section class="spread spread--inside" aria-label="Brochure inside">
  <div class="panel panel--athlete">
    <div class="photo photo--athlete" role="img" aria-label="Photo of a female athlete in red sportswear holding a dumbbell"></div>
  </div>

  <div class="panel panel--about">
    <h2 class="heading">About PeakForge Northwood</h2>
    <p class="body-copy">PeakForge Northwood is a strength and conditioning gym built on constantly varied, functional movement performed at high intensity. Our classes blend lifting, gymnastics and conditioning so every athlete grows stronger, faster and more capable in daily life.</p>
    <p class="body-copy">Every workout is scaled to your level, so beginners and seasoned athletes train side by side under the eye of certified coaches.</p>
    <h2 class="heading">Schedule / Programs</h2>
    <p class="body-copy">Classes run seven days a week, from early morning sessions before work to evening classes after it. Open gym hours let members practice skills on their own.</p>
  </div>

  <div class="panel panel--schedule">
    <p class="body-copy">Mon to Fri: 6am, 7am, 12pm, 5pm, 6pm and 7pm. Saturday: 9am and 10am. Sunday: 10am open gym. Arrive ten minutes early for your first class and bring water.</p>
    <p class="body-copy">No experience is needed. Our foundations course teaches the core movements safely before you join regular classes.</p>
  </div>

  <svg class="wave" viewBox="0 0 600 80" preserveAspectRatio="none" aria-hidden="true">
    <path d="M0 30 C150 10 300 50 450 28 C520 18 570 22 600 26 L600 80 L0 80 Z" fill="var(--red)"/>
    <path d="M0 30 C150 10 300 50 450 28 C520 18 570 22 600 26" fill="none" stroke="var(--white)" stroke-width="1.5"/>
  </svg>
  <span class="slogan slogan--start">Get Started Now!</span>
  <span class="slogan slogan--best">The Best Fit of your Life!</span>
</section>

</body>
</html>
```